existing Business Card Re design

We are wanting to re design our cards to reflect our new logo , i have attache the current business cards and new logo
i will need a business card that reflects the following information on each card.

card 1:
Gordon Thibeaux, President
555-182-4407
info@qlmcoatingpro.example

card 2:
Lionel Ostrander, Outside Sales
Office: 555-182-4407
Cell: 555-631-2958
Sales@qlmcoatingpro.example

Card 3
Tomas Varley, Branch Manager
Office: 555-182-4407
Cell: 555-274-8163
Tomas@qlmcoatingpro.example

Card 4
I will need a Generic card with no name on it just business
555-182-4407
info@qlmcoatingpro.example

Target Market(s)

Homeowners and Contractors

Contact Information for Business Card

We are wanting to re design our cards to reflect our new logo , i have attache the current business cards and new logo. same info on current card

card 1:
Gordon Thibeaux, President
555-182-4407
info@qlmcoatingpro.example

card 2:
Office: 555-182-4407
Cell: 555-631-2958
Sales@qlmcoatingpro.example

Card 3
Office: 555-182-4407
Cell: 555-274-8163
Tomas@qlmcoatingpro.example

Card 4
555-182-4407
info@qlmcoatingpro.example

Requirements
Must have
• same info as current cards with a added business
"sanitizing"

```html
<!DOCTYPE html>
<html lang="en">
<head>
<meta charset="utf-8">
<title>QLM Coating Pro – Business Cards</title>
<link rel="stylesheet" href="https://fonts.googleapis.com/css2?family=Archivo:ital,wght@0,400;0,800;0,900;1,800&family=Roboto:wght@300;400;500&display=swap">
<style>
  :root {
    --page-bg: #e9ebee;
    --card-white: #f2f3f4;
    --ink-black: #0a0b0c;
    --brand-blue: #1a9fd0;
    --brand-cyan: #27bde2;
    --brand-navy: #0a2a55;
    --deep-navy: #05131f;
    --stripe-light: #6cc3dd;
    --stripe-dark: #5a98b2;
    --text-light: #ffffff;
    --text-muted: #b9c6cf;
    --text-dark: #222222;
  }
  * { box-sizing: border-box; margin: 0; padding: 0; }
  html, body { width: 1200px; height: 780px; overflow: hidden; }
  body {
    background: var(--page-bg);
    font-family: "Archivo", sans-serif;
    position: relative;
  }
  .card-sheet {
    position: absolute; left: 30px; top: 169px;
    display: grid;
    grid-template-columns: repeat(3, 360px);
    grid-template-rows: repeat(2, 206px);
    column-gap: 30px; row-gap: 30px;
  }
  .card {
    position: relative;
    width: 360px; height: 206px;
    overflow: hidden;
    background: var(--card-white);
    box-shadow: 0 8px 20px rgba(10, 30, 50, 0.2);
  }

  /* ---------- Brand name ---------- */
  .brand-name {
    display: flex; align-items: center; gap: 8px;
    font-weight: 900; font-size: 21px; line-height: 1;
    color: var(--brand-navy); letter-spacing: -0.2px; white-space: nowrap;
  }
  .brand-name__square { width: 21px; height: 21px; background: var(--brand-navy); flex: none; }

  /* ---------- Front cards ---------- */
  .front__identity { position: absolute; left: 0; top: 0; width: 100%; height: 110px; }
  .front__identity .brand-name { position: absolute; left: 20px; top: 62px; }
  .card--generic .front__identity .brand-name { top: 44px; }
  .person { position: absolute; right: 20px; top: 22px; text-align: right; }
  .person__name {
    font-weight: 800; font-style: italic; font-size: 13px; line-height: 1.1;
    color: var(--brand-blue); text-transform: uppercase; letter-spacing: 0.2px; white-space: nowrap;
  }
  .person__title {
    font-family: "Roboto", sans-serif; font-weight: 400; font-size: 9px;
    color: var(--text-dark); margin-top: 2px;
  }
  .tagline-bar {
    position: absolute; left: 0; top: 110px; width: 100%; height: 18px;
    background: var(--ink-black);
    display: flex; align-items: center; padding-left: 14px;
  }
  .tagline {
    font-weight: 900; font-size: 10.5px; letter-spacing: 0.3px; line-height: 1;
    text-transform: uppercase; color: var(--text-light); white-space: nowrap;
  }
  .front__contact-band {
    position: absolute; left: 0; top: 128px; width: 100%; height: 78px;
    background: linear-gradient(90deg, var(--brand-cyan) 0%, #1690bd 45%, #0b4666 80%, var(--deep-navy) 100%);
  }
  .contact-list {
    position: absolute; left: 14px; top: 10px; list-style: none;
    font-family: "Roboto", sans-serif; font-size: 9.5px; color: var(--text-light);
  }
  .contact-list li { display: flex; align-items: center; gap: 6px; height: 14.5px; white-space: nowrap; }
  .contact-icon {
    width: 11px; height: 11px; border-radius: 50%; flex: none;
    background: rgba(255,255,255,0.85); display: flex; align-items: center; justify-content: center;
  }
  .contact-icon svg { width: 7px; height: 7px; }
  .address {
    position: absolute; right: 14px; top: 12px; text-align: right;
    font-family: "Roboto", sans-serif; font-size: 9px; line-height: 14px; color: var(--text-light);
    white-space: nowrap;
  }
  .address__web { font-weight: 500; }

  /* ---------- Back card ---------- */
  .back__top-band {
    position: absolute; left: 0; top: 0; width: 100%; height: 50px;
    background: linear-gradient(90deg, var(--brand-cyan) 0%, var(--brand-blue) 60%, #1a86b8 100%);
    display: flex; align-items: center; justify-content: center;
  }
  .back__top-band .tagline { color: var(--ink-black); font-size: 12px; }
  .stripe { position: absolute; left: 0; width: 100%; height: 6px; background: var(--stripe-light); }
  .stripe--top { top: 50px; }
  .stripe--bottom { top: 140px; background: var(--stripe-dark); }
  .back__logo-area {
    position: absolute; left: 0; top: 56px; width: 100%; height: 84px;
    display: flex; align-items: center; justify-content: center;
  }
  .back__logo-area .brand-name { font-size: 25px; }
  .back__logo-area .brand-name__square { width: 25px; height: 25px; }
  .back__bottom-band {
    position: absolute; left: 0; top: 146px; width: 100%; height: 60px;
    background: linear-gradient(90deg, var(--deep-navy) 0%, #0b3552 55%, #135d82 100%);
    display: flex; flex-direction: column; align-items: center; justify-content: center; gap: 6px;
  }
  .services {
    font-weight: 800; font-size: 8.8px; letter-spacing: 0.2px; line-height: 1;
    text-transform: uppercase; color: var(--text-light); white-space: nowrap;
  }
  .website {
    font-family: "Roboto", sans-serif; font-weight: 300; font-size: 8.5px; line-height: 1;
    letter-spacing: 2px; color: var(--text-muted);
  }
</style>
</head>
<body>
  <main class="card-sheet">

    <!-- Card 1 -->
    <section class="card card--front">
      <div class="front__identity">
        <div class="brand-name"><span class="brand-name__square"></span>QLM Coating Pro</div>
        <div class="person">
          <div class="person__name">Gordon Thibeaux</div>
          <div class="person__title">President</div>
        </div>
      </div>
      <div class="tagline-bar"><span class="tagline">DFW Premier Insulation Company</span></div>
      <div class="front__contact-band">
        <ul class="contact-list">
          <li><span class="contact-icon"><svg viewBox="0 0 24 24"><path fill="#1585b3" d="M6.6 10.8a15 15 0 0 0 6.6 6.6l2.2-2.2a1 1 0 0 1 1-.25 11.4 11.4 0 0 0 3.6.57 1 1 0 0 1 1 1V20a1 1 0 0 1-1 1A17 17 0 0 1 3 4a1 1 0 0 1 1-1h3.5a1 1 0 0 1 1 1c0 1.25.2 2.45.57 3.57a1 1 0 0 1-.25 1z"/></svg></span>555-182-4407</li>
          <li><span class="contact-icon"><svg viewBox="0 0 24 24"><rect x="2" y="5" width="20" height="14" rx="2" fill="#1585b3"/><path d="M3 6l9 7 9-7" fill="none" stroke="#fff" stroke-width="2"/></svg></span>info@qlmcoatingpro.example</li>
          <li><span class="contact-icon"></span>qlmcoatingpro</li>
        </ul>
        <div class="address">
          <div>4120 Alder Ridge Rd.</div>
          <div>Suite 5 Marlow, TX 75990</div>
          <div class="address__web">qlmcoatingpro.example</div>
        </div>
      </div>
    </section>

    <!-- Card 2 -->
    <section class="card card--front">
      <div class="front__identity">
        <div class="brand-name"><span class="brand-name__square"></span>QLM Coating Pro</div>
        <div class="person">
          <div class="person__name">Lionel Ostrander</div>
          <div class="person__title">Outside Sales</div>
        </div>
      </div>
      <div class="tagline-bar"><span class="tagline">DFW Premier Insulation Company</span></div>
      <div class="front__contact-band">
        <ul class="contact-list">
          <li><span class="contact-icon"><svg viewBox="0 0 24 24"><path fill="#1585b3" d="M6.6 10.8a15 15 0 0 0 6.6 6.6l2.2-2.2a1 1 0 0 1 1-.25 11.4 11.4 0 0 0 3.6.57 1 1 0 0 1 1 1V20a1 1 0 0 1-1 1A17 17 0 0 1 3 4a1 1 0 0 1 1-1h3.5a1 1 0 0 1 1 1c0 1.25.2 2.45.57 3.57a1 1 0 0 1-.25 1z"/></svg></span>Office: 555-182-4407</li>
          <li><span class="contact-icon"><svg viewBox="0 0 24 24"><path fill="#1585b3" d="M6.6 10.8a15 15 0 0 0 6.6 6.6l2.2-2.2a1 1 0 0 1 1-.25 11.4 11.4 0 0 0 3.6.57 1 1 0 0 1 1 1V20a1 1 0 0 1-1 1A17 17 0 0 1 3 4a1 1 0 0 1 1-1h3.5a1 1 0 0 1 1 1c0 1.25.2 2.45.57 3.57a1 1 0 0 1-.25 1z"/></svg></span>Cell: 555-631-2958</li>
          <li><span class="contact-icon"><svg viewBox="0 0 24 24"><rect x="2" y="5" width="20" height="14" rx="2" fill="#1585b3"/><path d="M3 6l9 7 9-7" fill="none" stroke="#fff" stroke-width="2"/></svg></span>Sales@qlmcoatingpro.example</li>
          <li><span class="contact-icon"></span>qlmcoatingpro</li>
        </ul>
        <div class="address">
          <div>4120 Alder Ridge Rd.</div>
          <div>Suite 5 Marlow, TX 75990</div>
          <div class="address__web">qlmcoatingpro.example</div>
        </div>
      </div>
    </section>

    <!-- Card 3 -->
    <section class="card card--front">
      <div class="front__identity">
        <div class="brand-name"><span class="brand-name__square"></span>QLM Coating Pro</div>
        <div class="person">
          <div class="person__name">Tomas Varley</div>
          <div class="person__title">Branch Manager</div>
        </div>
      </div>
      <div class="tagline-bar"><span class="tagline">DFW Premier Insulation Company</span></div>
      <div class="front__contact-band">
        <ul class="contact-list">
          <li><span class="contact-icon"><svg viewBox="0 0 24 24"><path fill="#1585b3" d="M6.6 10.8a15 15 0 0 0 6.6 6.6l2.2-2.2a1 1 0 0 1 1-.25 11.4 11.4 0 0 0 3.6.57 1 1 0 0 1 1 1V20a1 1 0 0 1-1 1A17 17 0 0 1 3 4a1 1 0 0 1 1-1h3.5a1 1 0 0 1 1 1c0 1.25.2 2.45.57 3.57a1 1 0 0 1-.25 1z"/></svg></span>Office: 555-182-4407</li>
          <li><span class="contact-icon"><svg viewBox="0 0 24 24"><path fill="#1585b3" d="M6.6 10.8a15 15 0 0 0 6.6 6.6l2.2-2.2a1 1 0 0 1 1-.25 11.4 11.4 0 0 0 3.6.57 1 1 0 0 1 1 1V20a1 1 0 0 1-1 1A17 17 0 0 1 3 4a1 1 0 0 1 1-1h3.5a1 1 0 0 1 1 1c0 1.25.2 2.45.57 3.57a1 1 0 0 1-.25 1z"/></svg></span>Cell: 555-274-8163</li>
          <li><span class="contact-icon"><svg viewBox="0 0 24 24"><rect x="2" y="5" width="20" height="14" rx="2" fill="#1585b3"/><path d="M3 6l9 7 9-7" fill="none" stroke="#fff" stroke-width="2"/></svg></span>Tomas@qlmcoatingpro.example</li>
          <li><span class="contact-icon"></span>qlmcoatingpro</li>
        </ul>
        <div class="address">
          <div>4120 Alder Ridge Rd.</div>
          <div>Suite 5 Marlow, TX 75990</div>
          <div class="address__web">qlmcoatingpro.example</div>
        </div>
      </div>
    </section>

    <!-- Card 4: generic -->
    <section class="card card--front card--generic">
      <div class="front__identity">
        <div class="brand-name"><span class="brand-name__square"></span>QLM Coating Pro</div>
      </div>
      <div class="tagline-bar"><span class="tagline">DFW Premier Insulation Company</span></div>
      <div class="front__contact-band">
        <ul class="contact-list">
          <li><span class="contact-icon"><svg viewBox="0 0 24 24"><path fill="#1585b3" d="M6.6 10.8a15 15 0 0 0 6.6 6.6l2.2-2.2a1 1 0 0 1 1-.25 11.4 11.4 0 0 0 3.6.57 1 1 0 0 1 1 1V20a1 1 0 0 1-1 1A17 17 0 0 1 3 4a1 1 0 0 1 1-1h3.5a1 1 0 0 1 1 1c0 1.25.2 2.45.57 3.57a1 1 0 0 1-.25 1z"/></svg></span>555-182-4407</li>
          <li><span class="contact-icon"><svg viewBox="0 0 24 24"><rect x="2" y="5" width="20" height="14" rx="2" fill="#1585b3"/><path d="M3 6l9 7 9-7" fill="none" stroke="#fff" stroke-width="2"/></svg></span>info@qlmcoatingpro.example</li>
          <li><span class="contact-icon"></span>qlmcoatingpro</li>
        </ul>
        <div class="address">
          <div>4120 Alder Ridge Rd.</div>
          <div>Suite 5 Marlow, TX 75990</div>
          <div class="address__web">qlmcoatingpro.example</div>
        </div>
      </div>
    </section>

    <!-- Shared back -->
    <section class="card card--back">
      <div class="back__top-band"><span class="tagline">DFW Premier Insulation Company</span></div>
      <div class="stripe stripe--top"></div>
      <div class="back__logo-area">
        <div class="brand-name"><span class="brand-name__square"></span>QLM Coating Pro</div>
      </div>
      <div class="stripe stripe--bottom"></div>
      <div class="back__bottom-band">
        <div class="services">Spray Foam | Fiberglass | Insulation | Roofing | Sanitizing</div>
        <div class="website">qlmcoatingpro.example</div>
      </div>
    </section>

  </main>
</body>
</html>
```